Saltwater In store poster design

We need a poster design that will be hung in aquarium stores, to advertise that they use our natural saltwater.

Must use logo as well as be bright and colourful. We are trying to communicate that the water is natural (so good for your marine tank) as well as clean and safe, so please consider this in your design.

Must say something along the lines of "We use natural ocean water supplied by Reef Bucket in our store" as well as "you can purchase natural ocean water here"

Open to all design types and suggestions as we will update the brief if we find one specific style that we prefer.

Target Market(s)

Customers who own marine aquariums

Industry/Entity Type

Store

Requirements
Must have
• Reef bucket logo (does not need to have blue background attached, just the oval)

Be eye catching

Have similar phrases to those above

```html
<!DOCTYPE html>
<html lang="en">
<head>
<meta charset="utf-8">
<title>Reef Bucket – Natural Ocean Water Poster</title>
<link rel="stylesheet" href="https://fonts.googleapis.com/css2?family=Comfortaa:wght@400;700&display=swap">
<style>
  :root {
    --sea-surface: #5ed3dc;
    --sea-mid: #1fa3c4;
    --sea-deep: #1a8fb9;
    --sand-light: #c9ece4;
    --sand-mid: #9fdbd4;
    --ink-white: #ffffff;
    --ink-teal: #45b4c3;
    --ink-deep-teal: #3b7f8f;
    --ink-shadow: rgba(10, 60, 80, 0.45);
  }
  * { margin: 0; padding: 0; box-sizing: border-box; }
  html, body { width: 783px; height: 1200px; overflow: hidden; background: #ffffff; }
  .poster {
    position: relative;
    width: 783px;
    height: 1200px;
    overflow: hidden;
    font-family: "Comfortaa", sans-serif;
    text-align: center;
  }
  .seascape {
    position: absolute;
    inset: 0;
    background:
      linear-gradient(180deg,
        var(--sea-surface) 0%,
        #3dbfd2 22%,
        var(--sea-mid) 45%,
        var(--sea-deep) 62%,
        #3fb3c6 70%,
        var(--sand-mid) 82%,
        var(--sand-light) 100%);
  }
  .headline {
    position: absolute;
    top: 160px;
    left: 0;
    width: 100%;
    font-size: 70px;
    font-weight: 400;
    letter-spacing: 2px;
    color: var(--ink-teal);
    -webkit-text-stroke: 5px var(--ink-white);
    paint-order: stroke fill;
  }
  .supply-line {
    position: absolute;
    top: 258px;
    left: 0;
    width: 100%;
    font-size: 25px;
    font-weight: 700;
    line-height: 34px;
    letter-spacing: 1.5px;
    text-transform: uppercase;
    color: var(--ink-white);
  }
  .brand-name {
    position: absolute;
    top: 382px;
    left: 0;
    width: 100%;
    font-size: 40px;
    font-weight: 700;
    color: var(--ink-white);
  }
  .call-to-action {
    position: absolute;
    top: 960px;
    left: 0;
    width: 100%;
    font-size: 46px;
    font-weight: 400;
    line-height: 42px;
    letter-spacing: 1px;
    color: var(--ink-deep-teal);
    -webkit-text-stroke: 4px var(--ink-white);
    paint-order: stroke fill;
    text-shadow: 0 2px 3px var(--ink-shadow);
  }
</style>
</head>
<body>
  <main class="poster">
    <div class="seascape" role="img" aria-label="Underwater photograph of clear turquoise ocean with a small school of fish above a rippled sandy seabed"></div>
    <h1 class="headline">simple. pure.</h1>
    <p class="supply-line">We use natural ocean water supplied<br>by</p>
    <p class="brand-name">Reef Bucket</p>
    <p class="call-to-action">purchase your natrural<br>ocean water here</p>
  </main>
</body>
</html>
```